Studio Verra Brochure and menu

in need of a update look for salon brochure. Basically same information and format but a fresher design. Since the salon is now selling fashionable hair wigs, I would like to add the wigs logo in the front of the the brochure along with the "Studio Verra" name. I'm open to color and design. The "salon K" logo is not an official logo, so a slight deviation is okay. I would to keep the design soft and hair salon focused. Uploaded are a copy of the current brochure without the front fold image, word doc with updated menu, "Verra Wigs" official logo, and "salon K Hair Designers" unofficial logo.
Updates

 I think it's probably best not to add "Verra Wigs" The main focus is "Salon D Hair Designers." I think it's getting confusing. I jsut wanted a little symbol of the wig logo in a small space. The main focus is the salon services. Thanks                                 

Except for the order of the salon services and mission statement,..every thing can be rearranged. I uploaded an example of what I presently have as my brochure. I feel like I'm getting the same format with little changes especially in the front (I removed the image in the front). If any thing, I would love to have the front of the brochure different than what I had before. Studio Verra doesn't have to be In the Same location. Thanks so much.

Industry/Entity Type

Salon

```html
<!DOCTYPE html>
<html lang="en">
<head>
<meta charset="utf-8">
<title>Studio Verra — Salon Brochure and Cards</title>
<link rel="stylesheet" href="https://fonts.googleapis.com/css2?family=Questrial&family=Didact+Gothic&display=swap">
<style>
:root{
  --orange:#f7831f;
  --maroon:#7a1e2c;
  --ink:#1c1c1c;
  --white:#ffffff;
  --card-edge:#e2482a;
}
*{box-sizing:border-box;margin:0;padding:0}
html,body{width:1200px;height:799px;overflow:hidden;background:var(--white)}
body{position:relative;font-family:"Questrial",sans-serif;color:var(--ink)}
.brochure{position:absolute;left:0;top:0;width:1200px;height:463px;border:1px solid #555;overflow:hidden}
.brochure-bg{position:absolute;left:0;top:0}
.fold{position:absolute;top:0;height:463px;border-left:1px solid #bdbdbd}
.panel{position:absolute;top:0;height:463px}
.heading{font-size:10.5px;color:var(--maroon);margin:10px 0 3px;line-height:1.1}
.heading:first-child{margin-top:6px}
.on-orange .heading{color:var(--white);font-size:10px}
.row{display:flex;justify-content:space-between;font-size:6.6px;line-height:9.6px;font-family:"Didact Gothic",sans-serif}
.copy{font-size:6.1px;line-height:9.4px;font-family:"Didact Gothic",sans-serif}
.on-orange{color:var(--white)}
.list{list-style:none;font-size:6.1px;line-height:9.4px;font-family:"Didact Gothic",sans-serif}
.list li::before{content:"•";margin-right:6px}
.list.indent li{padding-left:4px}
.list.indent li::before{margin-right:24px}
.price-head{display:flex;justify-content:space-between;align-items:flex-end}
.price-head small{font-size:6.5px}
.art{position:absolute;border-radius:50% 50% 40% 40%}
.wordmark{font-family:"Questrial",sans-serif;white-space:nowrap}
.mission{position:absolute;left:10px;top:113px;width:185px;font-size:9.6px;line-height:24.3px}
.mission .wordmark{color:var(--maroon);font-size:11px}
.foot-mark{position:absolute;top:408px;width:180px;text-align:center;color:var(--white);font-size:24px;letter-spacing:1px}
.booking{position:absolute;left:812px;top:212px;width:180px;text-align:center;color:var(--maroon);font-size:8.4px;line-height:10.5px}
.booking .wordmark{display:block;font-size:17px;line-height:24px;margin-bottom:2px}
.hours{position:absolute;left:812px;top:302px;width:180px;text-align:center;font-size:10.6px;line-height:10.8px}
.hours .gap{height:11px}
.cover-mark{position:absolute;left:1010px;top:330px;width:180px;text-align:center;color:var(--maroon);font-size:28px}
.card{position:absolute;left:195px;width:191px;height:110px;border:1px solid var(--card-edge);overflow:hidden;background:var(--white)}
.card svg{position:absolute;left:0;top:0}
.card-services{position:absolute;left:8px;top:6px;font-size:5.6px;line-height:7px;font-weight:bold;text-transform:uppercase}
.card-mark{position:absolute;left:40px;top:38px;color:var(--maroon);font-size:13px}
.card-address{position:absolute;left:5px;top:60px;font-size:5.4px;line-height:7px;font-weight:bold}
.card-name{position:absolute;left:100px;top:62px;width:90px;text-align:center;color:var(--white);font-size:8.2px;line-height:9.6px}
.card-links{position:absolute;left:0;top:89px;width:191px;text-align:center;color:var(--white);font-size:5.2px;line-height:8px;font-weight:bold}
</style>
</head>
<body>

<section class="brochure">
  <svg class="brochure-bg" width="1200" height="463" viewBox="0 0 1200 463" aria-hidden="true">
    <rect x="0" y="0" width="200" height="30" fill="var(--orange)"/>
    <path fill="var(--orange)" d="M0 385 C60 380 140 395 200 402 C270 408 360 372 394 292 C410 240 380 180 388 100 C392 50 398 20 404 0 H800 C812 80 838 150 828 205 C818 255 796 282 800 330 C805 380 880 405 1000 400 C1080 398 1150 390 1200 386 V463 H0 Z"/>
    <line x1="215" y1="432" x2="375" y2="432" stroke="var(--white)" stroke-width="0.8"/>
    <line x1="215" y1="436" x2="375" y2="436" stroke="var(--white)" stroke-width="0.8"/>
    <line x1="815" y1="432" x2="975" y2="432" stroke="var(--white)" stroke-width="0.8"/>
    <line x1="815" y1="436" x2="975" y2="436" stroke="var(--white)" stroke-width="0.8"/>
  </svg>

  <div class="fold" style="left:200px"></div>
  <div class="fold" style="left:400px"></div>
  <div class="fold" style="left:600px;border-left-color:#555"></div>
  <div class="fold" style="left:800px"></div>
  <div class="fold" style="left:1000px"></div>

  <!-- Panel: mission -->
  <div class="art" role="img" aria-label="Flowing hair illustration in maroon and orange" style="left:18px;top:8px;width:70px;height:86px;background:linear-gradient(135deg,#7a1e2c 0%,#b8452c 55%,#f7831f 100%)"></div>
  <p class="mission">Our mission at <span class="wordmark">Studio Verra</span> is to stay on the cutting edge of hair design. We promote optimum strength, integrity and healthy hair with only the finest hair care products as well as expert execution of chemical processes and thermal practices. Clients can expect a clean and comfortable environment while getting all their hair needs met.</p>

  <!-- Panel: styling menu -->
  <div class="panel" style="left:213px;width:165px">
    <h2 class="heading">Hair Styling</h2>
    <div class="row"><span>Shampoo/Blowdry/Curl or Flat Iron</span><span>$50 up</span></div>
    <div class="row"><span>Shampoo/Blowdry/Press/Curl or Flat Iron</span><span>$55 up</span></div>
    <div class="row"><span>Wet Set $45</span></div>
    <h2 class="heading">Relaxer/Permanent Wave</h2>
    <div class="row"><span>Virgin Relaxer</span><span>$120 up</span></div>
    <div class="row"><span>Relaxer Touch-Up</span><span>$75</span></div>
    <div class="row"><span>Edge Touch-Up</span><span>$25</span></div>
    <div class="row"><span>Permanent Waves/Curl</span><span>$85 up</span></div>
    <div class="row"><span>Japanese Straightening</span><span>$275 up</span></div>
    <div class="row"><span>Brazilian Straightening</span><span>$150 up</span></div>
    <h2 class="heading">High Fashion Styling</h2>
    <div class="row"><span>Add-on price from</span><span>$10-15</span></div>
    <div class="row"><span>Up-Do's - Ponytails - Spiral Curls</span></div>
    <div class="row"><span>Waves/Crimps - Flat Twist</span></div>
    <h2 class="heading">A LA Carte</h2>
    <div class="row"><span>Women's Haircut</span><span>$25 up</span></div>
    <div class="row"><span>Men's Haircut</span><span>$20</span></div>
    <div class="row"><span>Shampoo</span><span>$20</span></div>
    <div class="row"><span>Blowdry</span><span>$25</span></div>
    <div class="row"><span>Press</span><span>$35 up</span></div>
    <div class="row"><span>Curl</span><span>$35 up</span></div>
    <div class="row"><span>Flat Iron</span><span>$35 up</span></div>
    <h2 class="heading" style="margin-top:9px">Add-On services</h2>
    <h2 class="heading" style="margin-top:11px">Color</h2>
    <div class="row"><span>Demi/Semi-Permanent</span><span>$25 up</span></div>
    <div class="row"><span>Virgin Permanent</span><span>$65 up</span></div>
    <div class="row"><span>Retouch Permanent</span><span>$40 up</span></div>
    <div class="row"><span>Highlights</span></div>
    <div class="row"><span>Full</span><span>$110 up</span></div>
    <div class="row"><span>Partial</span><span>$65 up</span></div>
    <div class="row"><span>Individual Foils</span><span>$5 per foil</span></div>
  </div>
  <div class="foot-mark wordmark" style="left:205px">Studio Verra</div>

  <!-- Panel: packages and treatments -->
  <div class="panel on-orange" style="left:408px;width:160px">
    <h2 class="heading">Preferred Packages</h2>
    <p class="copy">Long or Thick hair additional price.</p>
    <h2 class="heading">Maintain #1</h2>
    <div class="row"><span>Relaxer touch-up/Lite trim/Finish</span><span>$90</span></div>
    <h2 class="heading">Maintain #2</h2>
    <div class="row"><span>Relaxer touch-up/Semi-color</span></div>
    <div class="row"><span>Lite Trim/Finish</span><span>$110</span></div>
    <h2 class="heading">Wedding Package</h2>
    <p class="copy">We will be happy to accommodate you and your wedding party in the salon or on location. Priced upon consultation.</p>
    <h2 class="heading">Intensive Hair &amp; Scalp Conditioning Treatments</h2>
    <p class="copy" style="width:185px">Hair and scalp conditioning treatments are recommended at least monthly to promote integrity and optimum health of hair and scalp. The finest products and natural plant extracts are used to replenish the vital elements that hair and scalp lose during wear and tear, heat and chemical processes. For added intensity, the hair steamer is used for most treatments.</p>
    <h2 class="heading price-head">Hot Oil Treatment <small>$15</small></h2>
    <p class="copy" style="width:185px">Formulated with naturally derived plant oils, this superior deep penetrating treatment adds new life to dry, dull and moisture-depleted hair. Essential ingredients of Jojoba Oil and Natural Honey lubricate to restore and maintain hair's natural moisture balance. Wheat protein strengthens hair, improving texture, body and shine.</p>
    <h2 class="heading price-head">2+1 Professional Deep Heat Reconstructor <small>$15</small></h2>
    <p class="copy" style="width:185px">A hair reconstructor that replenishes essential proteins, amino acids and humectants with a deep penetrating conditioning formula that restores texture, body and manageability.</p>
    <p class="copy">Recommended for those who:</p>
    <ul class="list"><li>Need on-going Reconstruction.</li><li>Have chemically relaxed hair.</li><li>Have overworked hair due to thermal styling.</li></ul>
  </div>

  <!-- Panel: conditioning and extensions -->
  <div class="panel on-orange" style="left:608px;width:168px">
    <h2 class="heading price-head">Restorix-Deep Conditioning Treatment <small>$15</small></h2>
    <p class="copy" style="width:180px">A deep penetrating conditioner that replenishes the vital elements that hair loses during chemical processes. Substantive proteins and polymeric additives bond with the hair for strength, shine and improved texture. Followed by a moisture treatment with humectants to attract moisture and lock in cuticles.</p>
    <p class="copy">Recommend for:</p>
    <ul class="list indent"><li>Same day relaxer service</li><li>Hair that lacks body</li><li>Hair that is shedding</li><li>Chemically processed hair</li><li>Maintaining healthy balanced hair</li></ul>
    <h2 class="heading price-head">Dry And flaky Scalp Conditioning Treatment <small>$15</small></h2>
    <p class="copy" style="width:182px">This conditioning treatment helps in controlling overactive sebaceous glands that cause sand-like dandruff or flakes resulting in dry and itchy scalp. The flakes are first lifted with a comb from front to back followed by a scalp antiseptic to lift any remaining flakes and stimulate the scalp. Next, hair is shampooed twice with tar especially formulated to reduce the build-up of dandruff. Essential oils are massaged into the scalp, rinsed, and then thermal cap conditioner is applied to further stimulate the scalp.</p>
    <h2 class="heading">Hair Extensions<br>And<br>Hair Replacement</h2>
    <p class="copy">Hot Fusion-Cold Fusion-Braid Weave-Lace-Bonding-Grafting</p>
    <p class="copy" style="width:182px">Prices are determined by consultation. Many factors determine the price of an individual seeking hair extension, weave or hair replacement such as:</p>
    <ul class="list"><li>Method used.</li><li>Hair texture.</li><li>Length of desired hair.</li><li>Color.</li><li>Quantity of hair attached.</li></ul>
  </div>

  <!-- Panel: extension services and hours -->
  <div class="panel" style="left:815px;width:158px">
    <h2 class="heading">Removal of Hair</h2>
    <div class="row"><span>Full</span><span>$45 up</span></div>
    <div class="row"><span>Partial</span><span>$3</span></div>
    <div class="row"><span>Tightening</span><span>$50 up</span></div>
    <h2 class="heading">Tracks</h2>
    <div class="row"><span>Braided, French, Bonded, Micro</span><span>$55 up</span></div>
    <h2 class="heading">Styling Extension Hair</h2>
    <div class="row"><span>Shampoo/Blowdry/Curl or Flat</span><span>$60</span></div>
    <div class="row"><span>Wet Set</span><span>$50</span></div>
    <h2 class="heading">A La Carte</h2>
    <div class="row"><span>Shampoo</span></div>
    <div class="row"><span>&nbsp;&nbsp;$20</span></div>
    <div class="row"><span>Blowdry</span><span>$30</span></div>
    <div class="row"><span>Curl/Flat Iron</span><span>$45 up</span></div>
  </div>
  <p class="booking"><span class="wordmark">Studio Verra</span>To best service clients, we recommend scheduling appointments at least one week in advance.</p>
  <div class="hours">
    <p>HOURS</p>
    <p>TUES - FRIDAY 10-8 PM</p>
    <p>SAT &nbsp;8-4</p>
    <div class="gap"></div>
    <p>949 555 0142</p>
    <p>2480 MEADOWLARK CIRCLE,SUITE K</p>
    <p>IRVINE, CA 92618</p>
  </div>
  <div class="foot-mark wordmark" style="left:805px">Studio Verra</div>

  <!-- Panel: cover -->
  <div class="art" role="img" aria-label="Large flowing hair illustration in maroon and orange" style="left:1040px;top:98px;width:122px;height:140px;background:linear-gradient(130deg,#7a1e2c 0%,#a43a2d 50%,#f7831f 100%)"></div>
  <div class="cover-mark wordmark">Studio Verra</div>
</section>

<!-- Business card, light art version -->
<article class="card" style="top:532px">
  <svg width="191" height="110" viewBox="0 0 191 110" aria-hidden="true">
    <path fill="var(--orange)" d="M110 0 H191 V110 H0 V80 C40 82 85 84 100 70 C112 58 98 40 110 25 C118 14 110 6 110 0 Z"/>
  </svg>
  <div class="art" role="img" aria-label="Flowing hair illustration in white" style="left:138px;top:6px;width:36px;height:54px;background:linear-gradient(140deg,#fff7ef,#fcd3ad)"></div>
  <p class="card-services">Hair relaxing / straightening<br>extensions/ weaves<br>cuts / custom color<br>wigs</p>
  <div class="card-mark wordmark">Studio Verra</div>
  <p class="card-address">2480 Meadowlark Circle,<br>Suite K Irvine, CA 92618<br>(949) 555-0142</p>
  <p class="card-name">MIRANDA COLE<br>OWNER / STYLIST</p>
  <p class="card-links">Email: hello@studioverra.com<br>www.studioverra.com - www.verrawigs.com</p>
</article>

<!-- Business card, dark art version -->
<article class="card" style="top:685px">
  <svg width="191" height="110" viewBox="0 0 191 110" aria-hidden="true">
    <path fill="var(--orange)" d="M110 0 H191 V110 H0 V80 C40 82 85 84 100 70 C112 58 98 40 110 25 C118 14 110 6 110 0 Z"/>
  </svg>
  <div class="art" role="img" aria-label="Flowing hair illustration in maroon and orange" style="left:138px;top:6px;width:36px;height:54px;background:linear-gradient(140deg,#7a1e2c,#c4542a)"></div>
  <p class="card-services">Hair relaxing / straightening<br>extensions/ weaves<br>cuts / custom color<br>wigs</p>
  <div class="card-mark wordmark">Studio Verra</div>
  <p class="card-address">2480 Meadowlark Circle,<br>Suite K Irvine, CA 92618<br>(949) 555-0142</p>
  <p class="card-name">MIRANDA COLE<br>OWNER / STYLIST</p>
  <p class="card-links">Email: hello@studioverra.com<br>www.studioverra.com - www.verrawigs.com</p>
</article>

</body>
</html>
```